Post card for landscape service

Velbrin Estate Management**FEATURED SERVICE*** Weekly Lawn mowing service starting at $15/ cutting ****other services****landscape servicespring and fall clean uplawn and flowerbed care (pest and weed control)fertilizing plantingand moreCall for a Free estimate!!10% off first months service with signed contract

Please make double sided ( a front and a back)

Target Market(s)

home owners

Industry/Entity Type

Landscape

Requirements
Must have
• please feture the weekly lawn mowing service and then list the other sevices
• contact info... can be found on business card that was uploaded.
• must say residential services
Should not have
• please dont list reo management

```html
<!DOCTYPE html>
<html lang="en">
<head>
<meta charset="utf-8">
<title>Velbrin Estate Management – Postcard</title>
<link href="https://fonts.googleapis.com/css2?family=Saira:wght@500;600;700&family=Oswald:wght@300;400;500&family=Lato:wght@400;700&family=Michroma&display=swap" rel="stylesheet">
<style>
  :root{
    --backdrop:#2b2b2b;
    --green:#3fb45f;
    --green-dark:#24a046;
    --blue:#1e86c8;
    --blue-ring:#1a7fc4;
    --ink:#1d1d1d;
    --white:#ffffff;
    --red:#e8272a;
  }
  *{box-sizing:border-box;margin:0;padding:0}
  html,body{width:900px;height:1200px;overflow:hidden;background:var(--backdrop)}
  .canvas{position:relative;width:900px;height:1200px}
  .card{position:absolute;left:76px;width:747px;height:538px;overflow:hidden}

  /* FRONT */
  .front{top:47px;background:linear-gradient(180deg,#54b96f 0%,#3fae5e 55%,#5fbf78 100%)}
  .front .header{position:absolute;left:0;top:0;width:420px;height:141px;background:var(--white)}
  .brand-mark{position:absolute;left:32px;top:18px;width:110px;text-align:center}
  .brand-mark .dot{display:block;width:70px;height:70px;margin:0 auto 10px;border-radius:50%;background:var(--ink)}
  .brand-mark .name{font:400 12px/1 "Lato",sans-serif;color:var(--ink);letter-spacing:.3px}
  .front .title{position:absolute;left:171px;top:46px;font:600 22px/1.28 "Saira",sans-serif;color:var(--ink)}
  .front .title .accent{color:var(--green-dark)}
  .front .segment{position:absolute;left:171px;top:118px;font:300 13px/1 "Oswald",sans-serif;color:var(--ink)}
  .banner{position:absolute;left:0;top:175px;width:286px;height:40px;background:var(--blue);color:var(--white);
    font:400 27px/40px "Oswald",sans-serif;padding-left:40px;letter-spacing:.2px}
  .services{position:absolute;left:22px;top:231px;width:330px;list-style:none}
  .services li{position:relative;padding-left:29px;margin-bottom:6px;font:400 18.5px/26px "Lato",sans-serif;color:var(--white);white-space:nowrap}
  .services svg{position:absolute;left:0;top:3px;width:20px;height:20px}
  .services .price{color:var(--red);font-size:23px;font-weight:700;line-height:26px}
  .services .offer{color:var(--red)}
  .call-bar{position:absolute;left:0;top:493px;width:394px;height:33px;background:var(--blue);color:var(--white);
    font:600 20px/33px "Saira",sans-serif;padding-left:50px;letter-spacing:.8px;display:flex;align-items:center;gap:8px}
  .call-bar svg{width:20px;height:20px}
  .photo-ring{position:absolute;left:355px;top:25px;width:440px;height:495px;border-radius:50%;border:9px solid var(--blue-ring);
    background:linear-gradient(160deg,#e9eef2 0%,#c9d7c4 30%,#a06cc8 58%,#e58a2a 75%,#3f7d3a 100%);overflow:hidden}

  /* BACK */
  .back{top:622px;background:var(--white)}
  .back .swoosh{position:absolute;left:0;top:0;width:747px;height:538px}
  .back-copy{position:absolute;left:37px;top:30px;width:360px}
  .back .title{font:600 21px/1.3 "Saira",sans-serif;color:var(--ink)}
  .back .title .accent{color:var(--green-dark)}
  .back .intro{margin-top:12px;font:400 17.5px/24px "Lato",sans-serif;color:var(--ink)}
  .offerings{list-style:none;margin-top:12px}
  .offerings li{position:relative;padding-left:22px;font:400 15px/26.5px "Michroma",sans-serif;color:var(--ink)}
  .offerings svg{position:absolute;left:0;top:6px;width:15px;height:15px}
  .contact{position:absolute;left:39px;top:362px;font:400 19px/1.38 "Lato",sans-serif;color:var(--ink);font-style:normal}
  .contact .row{display:flex;align-items:center;gap:6px}
  .contact svg{width:15px;height:15px;flex:none}
  .contact .gap{margin-top:4px}
  .contact .web{font-size:17px}
  .contact-tag{position:absolute;left:220px;top:336px;width:168px;height:64px}
  .contact-tag span{position:absolute;left:0;top:4px;width:160px;text-align:center;font:400 24px/36px "Oswald",sans-serif;color:var(--white)}
  .stamp{position:absolute;left:640px;top:30px;width:78px;height:84px;border:1px solid #444}
</style>
</head>
<body>
<main class="canvas">

  <section class="card front" aria-label="Postcard front">
    <div class="photo-ring" role="img" aria-label="Photo of a landscaped walkway with a flowering white tree, purple azaleas, orange tulips and a trimmed hedge"></div>

    <header class="header">
      <div class="brand-mark">
        <span class="dot"></span>
        <span class="name">Velbrin Estate</span>
      </div>
      <h1 class="title"><span class="accent">Velbrin</span> Estate<br>Management</h1>
      <p class="segment">Commercial &amp; Residential</p>
    </header>

    <div class="banner">FEATURED SERVICE</div>

    <ul class="services">
      <li><svg viewBox="0 0 20 20"><circle cx="10" cy="10" r="8.5" fill="none" stroke="#fff" stroke-width="1.8"/><path d="M6 10.5l3 3 8-8" fill="none" stroke="#fff" stroke-width="2"/></svg>Weekly Lawn mowing service<br>starting at <span class="price">$15</span></li>
      <li><svg viewBox="0 0 20 20"><circle cx="10" cy="10" r="8.5" fill="none" stroke="#fff" stroke-width="1.8"/><path d="M6 10.5l3 3 8-8" fill="none" stroke="#fff" stroke-width="2"/></svg>Cuttingother serviceslandscape<br>servicespring</li>
      <li><svg viewBox="0 0 20 20"><circle cx="10" cy="10" r="8.5" fill="none" stroke="#fff" stroke-width="1.8"/><path d="M6 10.5l3 3 8-8" fill="none" stroke="#fff" stroke-width="2"/></svg>Fall clean uplawn and flowerbed<br>care (pest and weed control)</li>
      <li><svg viewBox="0 0 20 20"><circle cx="10" cy="10" r="8.5" fill="none" stroke="#fff" stroke-width="1.8"/><path d="M6 10.5l3 3 8-8" fill="none" stroke="#fff" stroke-width="2"/></svg>Fertilizing plantingand moreCall<br>for a Free estimate!! <span class="offer">10% off</span> first<br>months service with signed contract</li>
    </ul>

    <div class="call-bar">Call Now
      <svg viewBox="0 0 20 20"><circle cx="10" cy="10" r="9" fill="none" stroke="#e8272a" stroke-width="1.6"/><path d="M7 5.5l2 2.2-1 1.3c.6 1.3 1.6 2.3 2.9 2.9l1.3-1 2.2 2-1.1 1.6C9.6 14.2 5.8 10.4 5.4 6.6z" fill="#e8272a"/></svg>
      555-014-2290</div>
  </section>

  <section class="card back" aria-label="Postcard back">
    <svg class="swoosh" viewBox="0 0 747 538" aria-hidden="true">
      <defs>
        <linearGradient id="skyFade" x1="0" y1="0" x2="1" y2="0">
          <stop offset="0" stop-color="#c7e4f7"/>
          <stop offset="1" stop-color="#f4fafe"/>
        </linearGradient>
      </defs>
      <path d="M0 0H322C460 90 500 380 388 538H0Z" fill="url(#skyFade)"/>
      <path d="M322 0H350C500 100 520 390 405 538H388C500 380 460 90 322 0Z" fill="#3fb45f"/>
    </svg>

    <div class="stamp"></div>

    <div class="back-copy">
      <h2 class="title"><span class="accent">Velbrin</span><br>Estate Management</h2>
      <p class="intro">Velbrin Estate Management will help you manage you commercial properties with services ranging from landscaping, pest control, snow removal and more.</p>
      <ul class="offerings">
        <li><svg viewBox="0 0 20 20"><circle cx="10" cy="10" r="8.5" fill="none" stroke="#24a046" stroke-width="1.8"/><path d="M6 10.5l3 3 8-8" fill="none" stroke="#24a046" stroke-width="2"/></svg>Landscape Maintenance</li>
        <li><svg viewBox="0 0 20 20"><circle cx="10" cy="10" r="8.5" fill="none" stroke="#24a046" stroke-width="1.8"/><path d="M6 10.5l3 3 8-8" fill="none" stroke="#24a046" stroke-width="2"/></svg>Lawn Care</li>
        <li><svg viewBox="0 0 20 20"><circle cx="10" cy="10" r="8.5" fill="none" stroke="#24a046" stroke-width="1.8"/><path d="M6 10.5l3 3 8-8" fill="none" stroke="#24a046" stroke-width="2"/></svg>Property Preservation</li>
        <li><svg viewBox="0 0 20 20"><circle cx="10" cy="10" r="8.5" fill="none" stroke="#24a046" stroke-width="1.8"/><path d="M6 10.5l3 3 8-8" fill="none" stroke="#24a046" stroke-width="2"/></svg>Snow and Ice Management<br>and More</li>
      </ul>
    </div>

    <svg class="contact-tag" viewBox="0 0 168 64" aria-hidden="true">
      <path d="M10 0H164L152 44H114L108 62L100 44H0Z" fill="#24a046"/>
    </svg>
    <div class="contact-tag"><span>Contact Us</span></div>

    <address class="contact">
      <div class="row"><svg viewBox="0 0 16 16"><path d="M8 1a4.5 4.5 0 0 0-4.5 4.5C3.5 9 8 12 8 12s4.5-3 4.5-6.5A4.5 4.5 0 0 0 8 1z" fill="none" stroke="#24a046" stroke-width="1.6"/><circle cx="8" cy="5.5" r="1.6" fill="#24a046"/><path d="M3 15h10" stroke="#24a046" stroke-width="1.6"/></svg>PO Box 418</div>
      <div>Ashford Glen, NJ 07990</div>
      <div class="row gap"><svg viewBox="0 0 16 16"><circle cx="8" cy="8" r="7" fill="none" stroke="#24a046" stroke-width="1.4"/><path d="M5.6 4.4l1.5 1.7-.8 1c.5 1 1.2 1.7 2.2 2.2l1-.8 1.6 1.5-.8 1.2C7.6 11 5 8.4 4.7 5.6z" fill="#24a046"/></svg>555-017-3361
        <svg viewBox="0 0 16 16"><circle cx="8" cy="8" r="7" fill="none" stroke="#24a046" stroke-width="1.4"/><path d="M5.6 4.4l1.5 1.7-.8 1c.5 1 1.2 1.7 2.2 2.2l1-.8 1.6 1.5-.8 1.2C7.6 11 5 8.4 4.7 5.6z" fill="#24a046"/></svg>555-014-2290</div>
      <div class="row"><svg viewBox="0 0 16 16"><rect x="1.5" y="3.5" width="13" height="9" fill="none" stroke="#24a046" stroke-width="1.3"/><path d="M1.5 3.5L8 9l6.5-5.5" fill="none" stroke="#24a046" stroke-width="1.3"/></svg>velbrinestate@mail.com</div>
      <div class="row gap"><svg viewBox="0 0 16 16"><circle cx="8" cy="8" r="6.5" fill="none" stroke="#24a046" stroke-width="1.3"/><ellipse cx="8" cy="8" rx="2.8" ry="6.5" fill="none" stroke="#24a046" stroke-width="1.1"/><path d="M1.5 8h13" stroke="#24a046" stroke-width="1.1"/></svg><span class="web">www.VelbrinEstateManagement.com</span></div>
    </address>
  </section>

</main>
</body>
</html>
```